Health Coaching website focused on diabetes management using Plumcraft template

I am starting a health coaching business and would like to use Sitepress and an Plumcraft template. The coaching will focus on Pre-diabetic and chronic disease patients so it will need to have a personal as well as a slight clinical look to it. The site should have an overall look similar to Meadow Lantern theme. I will purchase the Plumcraft designer package for use.

Target Market(s)

40-60 year olds with pre-diabetes or concerned about chronic disease, maintaining health, nutrition and weight loss

Industry/Entity Type

Health And Wellness

Number of Pages Required

5+ page

Colors
87cfc6
60b9df
fee18a
00a990
3276b5

Requirements
Must have
• It should contain an ecommerce tab, member's only area, interactive blog, built-in SEO and an opt-in area on every page. It should have several call to actions throughout the site. The site should have an overall look similar to Meadow Lantern theme. Hosting on Webvault. Also needed all the essential sitepress plugins:
• Surge forms & Surge entry pages
• Zentro Metrics
• Plumcraft guard pro
• Postfinch
• Varondo
• Vault Pal
• Kirvo SEO
• Hovering Share Strip
• Q9 Swift Store
• Pelk
Nice to have
• Ecommerce ready with cartelia plugin
• Hi-res pictures of people in my demographic enjoying life and/or exercising, cooking, etc.
Should not have
• slider on homepage
• my profile on homepage

```html
<!DOCTYPE html>
<html lang="en">
<head>
<meta charset="utf-8">
<title>Contact Us – VitalPath For Wellness</title>
<link href="https://fonts.googleapis.com/css2?family=Jost:wght@400;500&family=Open+Sans:wght@400;600;700&display=swap" rel="stylesheet">
<style>
:root{
  --blue:#3577b8;
  --teal:#00a990;
  --teal-dark:#00967f;
  --ink:#222;
  --text:#333;
  --muted:#666;
  --line:#d5d5d5;
  --band:#f2f2f2;
  --crumb:#e6e6e6;
  --footer:#1e2631;
  --footer-text:#c9ced6;
  --red:#e03a3a;
}
*{box-sizing:border-box;margin:0;padding:0}
html,body{width:883px;height:1200px;overflow:hidden;background:#fff}
body{position:relative;font-family:"Open Sans",sans-serif;color:var(--text)}
.abs{position:absolute}
.heading{font-family:"Jost",sans-serif;font-weight:400}

/* header */
.brand{left:118px;top:10px;display:flex;align-items:center;gap:10px}
.brand-dot{width:52px;height:52px;border-radius:50%;background:var(--teal)}
.brand-name{font-family:"Jost",sans-serif;font-size:23px;line-height:27px;color:#2e2e2e}
.phone{left:460px;top:30px;display:flex;align-items:center;gap:10px;font-size:16px;color:#444}
.phone-icon{width:27px;height:27px;border-radius:50%;background:var(--teal);display:flex;align-items:center;justify-content:center}
.cta{left:604px;top:30px;width:160px;height:27px;background:var(--teal);border-bottom:2px solid var(--teal-dark);color:#fff;font-size:10.5px;display:flex;align-items:center;justify-content:center;gap:8px;letter-spacing:.2px}

/* nav */
.nav{left:0;top:83px;width:883px;height:27px;background:var(--blue)}
.nav ul{list-style:none;position:absolute;left:118px;top:0;height:27px;display:flex}
.nav li{height:27px;display:flex;align-items:center;justify-content:center;color:#fff;font-size:9.2px;font-weight:700;border-left:1px solid rgba(255,255,255,.18)}
.nav li.active{background:var(--teal)}

/* hero */
.hero{left:0;top:110px;width:883px;height:248px;background:linear-gradient(90deg,#e7e2d8 0%,#efece4 60%,#e9e6de 100%)}
.hero-photo{position:absolute;left:0;top:0;width:455px;height:248px;background:linear-gradient(135deg,#b8a48a 0%,#8e7458 45%,#6f8a3a 80%,#a8562f 100%)}
.hero-title{position:absolute;left:480px;top:48px;width:304px;text-align:center;font-family:"Jost",sans-serif;font-size:36px;line-height:46px;color:#111}
.hero-sub{position:absolute;left:480px;top:139px;width:304px;text-align:center;font-size:14px;line-height:17px;color:#222}
.dots{position:absolute;left:611px;top:197px;display:flex;gap:4px}
.dots span{width:8px;height:8px;border-radius:50%;background:#777}
.dots span.on{background:var(--teal)}

.crumb{left:0;top:358px;width:883px;height:29px;background:var(--crumb);font-size:9.5px;padding:9px 0 0 118px;color:#444}
.crumb b{color:#222}

/* contact intro */
.page-title{left:0;top:412px;width:883px;text-align:center;font-size:24px;color:var(--ink)}
.page-title span{color:var(--blue)}
.divider{left:269px;top:461px;width:346px;height:1px;background:#bbb}
.divider-mark{left:434px;top:454px;width:15px;height:15px;border-radius:50%;background:#fff;border:1px solid #aaa}
.intro{left:118px;top:478px;width:647px;text-align:center;font-size:9.5px;line-height:14.2px;color:#333}

/* form */
.label{font-size:9.5px;color:#333}
.label i{font-style:normal;color:var(--red)}
.field{border:1px solid #cfcfcf;background:#fff}
.send{left:118px;top:757px;width:68px;height:24px;background:var(--blue);border-bottom:2px solid #245e98;color:#fff;font-size:10.5px;display:flex;align-items:center;justify-content:center}
.map{left:441px;top:552px;width:324px;height:229px;background:linear-gradient(135deg,#ecebe6,#e2e1da 60%,#dfe6cf)}

/* info band */
.band{left:0;top:814px;width:883px;height:146px;background:var(--band)}
.info-title{font-size:14.5px;color:#222}
.info-rule{height:1px;background:#dcdcdc}
.info-text{font-size:8.8px;line-height:16px;color:#222}
.vline{width:1px;background:#d8d8d8;top:842px;height:92px}

/* footer */
.footer{left:0;top:960px;width:883px;height:206px;background:var(--footer)}
.f-head{font-size:13px;color:#fff;letter-spacing:.2px}
.f-head span{color:var(--teal)}
.f-rule{height:1px;background:#2f4a49}
.f-links{list-style:none;font-size:9.3px;line-height:15px;color:var(--footer-text)}
.f-links li::before{content:"›";margin-right:6px;color:#777}
.f-links li.on{color:var(--teal)}
.f-text{font-size:9.3px;line-height:15px;color:var(--footer-text)}
.f-line{display:flex;align-items:center;gap:8px;color:var(--footer-text)}
.social{display:flex;align-items:center;gap:8px;font-size:9.3px;color:var(--footer-text)}
.social span.c{width:22px;height:22px;border-radius:50%;border:2px solid #fff}
.f-brand{left:616px;top:1060px;width:150px;text-align:center;font-family:"Jost",sans-serif;font-size:20px;line-height:24px;color:#7c838c}
.bottom{left:0;top:1166px;width:883px;height:34px;background:var(--teal);color:#fff;font-size:9px;padding:11px 0 0 120px}
</style>
</head>
<body>

<header>
  <div class="abs brand">
    <span class="brand-dot"></span>
    <span class="brand-name">VitalPath<br>For Wellness</span>
  </div>
  <div class="abs phone">
    <span class="phone-icon"><svg width="13" height="13" viewBox="0 0 24 24"><path fill="#fff" d="M6.6 10.8c1.4 2.8 3.8 5.1 6.6 6.6l2.2-2.2c.3-.3.7-.4 1-.2 1.1.4 2.3.6 3.6.6.6 0 1 .4 1 1V20c0 .6-.4 1-1 1C10.6 21 3 13.4 3 4c0-.6.4-1 1-1h3.5c.6 0 1 .4 1 1 0 1.3.2 2.5.6 3.6.1.3 0 .7-.2 1z"/></svg></span>
    555-214-0387
  </div>
  <div class="abs cta">
    <svg width="12" height="12" viewBox="0 0 12 12"><rect x="1" y="2" width="10" height="9" fill="none" stroke="#fff"/><path d="M1 5h10M4 1v2M8 1v2" stroke="#fff"/></svg>
    MAKE AN APPOINTMENT
  </div>
</header>

<nav class="abs nav">
  <ul>
    <li style="width:53px">HOME</li>
    <li style="width:131px">ABOUT VITALPATH</li>
    <li style="width:90px">OUR COURSES</li>
    <li style="width:96px">SPECIAL OFFERS</li>
    <li style="width:91px">TESTIMONIALS</li>
    <li style="width:51px">BLOG</li>
    <li style="width:55px">FAQ'S</li>
    <li class="active" style="width:78px">CONTACT US</li>
  </ul>
</nav>

<section class="abs hero">
  <div class="hero-photo" role="img" aria-label="Photo of a smiling couple cooking with fresh vegetables in a home kitchen"></div>
  <div class="hero-title">VitalPath<br>For Wellness</div>
  <div class="hero-sub">Get the health and lifestyle<br>you want now!</div>
  <div class="dots"><span class="on"></span><span></span><span></span><span></span></div>
</section>

<div class="abs crumb">Home / <b>Contact Us</b></div>

<h1 class="abs heading page-title">Contact <span>Us</span></h1>
<div class="abs divider"></div>
<div class="abs divider-mark"></div>
<p class="abs intro">Lorem ipsum dolor smit amet, consectetuer adipiscing elitmk, sed amet diam nonummy nibh euismod tincidun ntl more utmn laoreetml dolore magna aliquam erat volutpat. Ut wisi enim ad minim veniam, quis nostrud exer tationk ullamcorik Lorem ipsum dolor smit amet, consectetuer adipiscing elitmk, sed amet diam nonummy nibh euismod tincidun ntl more utmn laoreetml dolore magna aliquam erat volutpat. Ut wisi enim ad minim veniam.</p>

<form>
  <label class="abs label" style="left:118px;top:555px">Name <i>*</i></label>
  <div class="abs field" style="left:118px;top:570px;width:144px;height:25px"></div>
  <label class="abs label" style="left:280px;top:555px">Email <i>*</i></label>
  <div class="abs field" style="left:280px;top:570px;width:144px;height:25px"></div>
  <label class="abs label" style="left:118px;top:605px">Phone <i>*</i></label>
  <div class="abs field" style="left:118px;top:621px;width:144px;height:25px"></div>
  <label class="abs label" style="left:280px;top:605px">Subject <i>*</i></label>
  <div class="abs field" style="left:280px;top:621px;width:144px;height:25px"></div>
  <label class="abs label" style="left:118px;top:655px">Message</label>
  <div class="abs field" style="left:118px;top:670px;width:306px;height:75px"></div>
  <div class="abs send">Send</div>
</form>

<div class="abs map" role="img" aria-label="Street map showing the office location with a blue marker"></div>

<section class="abs band"></section>
<div class="abs vline" style="left:165px"></div>
<div class="abs vline" style="left:386px"></div>
<div class="abs vline" style="left:606px"></div>

<svg class="abs" style="left:116px;top:862px" width="44" height="52" viewBox="0 0 44 52"><polygon points="22,2 40,12 40,36 22,46 4,36 4,12" fill="#fff" stroke="#3577b8" stroke-width="2"/><path d="M22 14a7 7 0 0 0-7 7c0 5 7 12 7 12s7-7 7-12a7 7 0 0 0-7-7z" fill="none" stroke="#3577b8" stroke-width="2"/><circle cx="22" cy="21" r="2.5" fill="#3577b8"/></svg>
<svg class="abs" style="left:336px;top:862px" width="44" height="52" viewBox="0 0 44 52"><polygon points="22,2 40,12 40,36 22,46 4,36 4,12" fill="#fff" stroke="#3577b8" stroke-width="2"/><rect x="12" y="16" width="20" height="15" fill="none" stroke="#3577b8" stroke-width="2"/><path d="M12 16l10 8 10-8" fill="none" stroke="#3577b8" stroke-width="2"/></svg>
<svg class="abs" style="left:556px;top:862px" width="44" height="52" viewBox="0 0 44 52"><polygon points="22,2 40,12 40,36 22,46 4,36 4,12" fill="#fff" stroke="#3577b8" stroke-width="2"/><path d="M14 20c0-3 16-3 16 0v2h-4v-2h-8v2h-4z M15 24h14v8H15z" fill="none" stroke="#3577b8" stroke-width="2"/><circle cx="22" cy="28" r="2" fill="#3577b8"/></svg>
<svg class="abs" style="left:164px;top:878px" width="8" height="16" viewBox="0 0 8 16"><path d="M1 1l6 7-6 7" fill="none" stroke="#00a990" stroke-width="1.5"/></svg>
<svg class="abs" style="left:385px;top:878px" width="8" height="16" viewBox="0 0 8 16"><path d="M1 1l6 7-6 7" fill="none" stroke="#00a990" stroke-width="1.5"/></svg>
<svg class="abs" style="left:605px;top:878px" width="8" height="16" viewBox="0 0 8 16"><path d="M1 1l6 7-6 7" fill="none" stroke="#00a990" stroke-width="1.5"/></svg>

<h3 class="abs heading info-title" style="left:181px;top:846px">Contact&nbsp; Details</h3>
<div class="abs info-rule" style="left:181px;top:876px;width:142px"></div>
<p class="abs info-text" style="left:184px;top:883px">123, Lorem Ipsum Dollar Smit Amet,<br>Nibh Nonumy. Golham - 123 456</p>

<h3 class="abs heading info-title" style="left:402px;top:846px">Email Address</h3>
<div class="abs info-rule" style="left:402px;top:876px;width:142px"></div>
<p class="abs info-text" style="left:405px;top:883px">info@vitalpath4wellness.com</p>

<h3 class="abs heading info-title" style="left:623px;top:846px">Contact No</h3>
<div class="abs info-rule" style="left:623px;top:876px;width:142px"></div>
<p class="abs info-text" style="left:626px;top:883px">555-214-0387<br>555-214-0391</p>

<footer class="abs footer"></footer>

<h4 class="abs heading f-head" style="left:118px;top:992px">QUICK&nbsp; <span>LINKS</span></h4>
<div class="abs f-rule" style="left:118px;top:1018px;width:90px"></div>
<ul class="abs f-links" style="left:118px;top:1027px">
  <li class="on">Home</li><li>About VitalPath</li><li>Our Courses</li><li>Special Offers</li><li>Testimonials</li><li>Blog</li><li>Faq's</li><li>Contact Us</li>
</ul>

<h4 class="abs heading f-head" style="left:240px;top:992px">CONTACT&nbsp; <span>DETAILS</span></h4>
<div class="abs f-rule" style="left:240px;top:1018px;width:144px"></div>
<p class="abs f-text" style="left:240px;top:1027px;color:#fff">VITALPATH FOR WELLNESS</p>
<p class="abs f-text" style="left:240px;top:1043px">123, Lorem Ipsum Dollar Smit Amet,<br>Nibh Nonumy. Golham - 123 456</p>
<div class="abs f-line" style="left:240px;top:1078px;font-size:11.5px">
  <svg width="10" height="10" viewBox="0 0 24 24"><path fill="#00a990" d="M6.6 10.8c1.4 2.8 3.8 5.1 6.6 6.6l2.2-2.2c.3-.3.7-.4 1-.2 1.1.4 2.3.6 3.6.6.6 0 1 .4 1 1V20c0 .6-.4 1-1 1C10.6 21 3 13.4 3 4c0-.6.4-1 1-1h3.5c.6 0 1 .4 1 1 0 1.3.2 2.5.6 3.6.1.3 0 .7-.2 1z"/></svg>555-214-0387</div>
<div class="abs f-line" style="left:239px;top:1103px;font-size:11.5px">
  <svg width="12" height="11" viewBox="0 0 12 11"><rect x="3" y="0" width="6" height="3" fill="#00a990"/><rect x="0" y="3" width="12" height="5" fill="#00a990"/><rect x="3" y="7" width="6" height="4" fill="#00a990"/></svg>555-214-0391</div>
<div class="abs f-line" style="left:240px;top:1133px;font-size:9.3px">
  <svg width="11" height="9" viewBox="0 0 11 9"><rect width="11" height="9" fill="#00a990"/><path d="M0 0l5.5 5L11 0" fill="none" stroke="#1e2631"/></svg>info@vitalpath4wellness.com</div>

<h4 class="abs heading f-head" style="left:417px;top:992px">FOLLOW&nbsp; <span>US</span></h4>
<div class="abs f-rule" style="left:417px;top:1018px;width:166px"></div>
<div class="abs social" style="left:423px;top:1036px"><span class="c" style="background:#3b5998"></span>Circlefeed</div>
<div class="abs social" style="left:423px;top:1065px"><span class="c" style="background:#2fa8dd"></span>Chirpline</div>
<div class="abs social" style="left:423px;top:1093px"><span class="c" style="background:#0e76a8"></span>Workweave</div>
<div class="abs social" style="left:423px;top:1126px"><span class="c" style="background:#d42a2a"></span>Orbitplus</div>

<div class="abs f-brand">VitalPath<br>For Wellness</div>

<div class="abs bottom">© 2016 VitalPath For Wellness. All Rights Reserved.</div>

</body>
</html>
```